Business Card for Pimortex

I need a creative Business Card design for my start-up.
Pimortex is a Vouchers (discounts) and media publisher, logo attached.
Info to be included:
First & Last name
Mobile Number
Email
Website
Social media accounts, Facebook, Insta, Linkedin.

```html
<!DOCTYPE html>
<html lang="en">
<head>
<meta charset="utf-8">
<title>Pimortex Business Card</title>
<link href="https://fonts.googleapis.com/css2?family=Cinzel:wght@500;700&family=Montserrat:wght@300;400;700&display=swap" rel="stylesheet">
<style>
  :root {
    --navy: #2b2a6b;
    --navy-deep: #22215a;
    --orange: #f08a1c;
    --paper: #f7f7f7;
    --ink: #3a3a3a;
    --rule: #c9c9c9;
    --stage: #d9d9d9;
  }
  * { margin: 0; padding: 0; box-sizing: border-box; }
  html, body { width: 1200px; height: 928px; overflow: hidden; }
  body {
    background: var(--stage);
    font-family: "Montserrat", Arial, sans-serif;
    position: relative;
  }
  .card {
    position: absolute;
    border-radius: 18px;
    overflow: hidden;
    box-shadow: 0 12px 30px rgba(0,0,0,0.18);
  }
  /* Back side */
  .card-back {
    left: 70px; top: 292px;
    width: 600px; height: 344px;
    background: linear-gradient(135deg, var(--navy) 0%, var(--navy-deep) 100%);
  }
  .card-back .emboss {
    position: absolute;
    left: 60px; top: 80px;
    width: 190px; height: 190px;
    border-radius: 50%;
    background: rgba(0,0,0,0.12);
    box-shadow: inset 1px 1px 2px rgba(255,255,255,0.06);
  }
  .card-back .wordmark {
    position: absolute;
    right: 44px; top: 142px;
    color: #ffffff;
    font-weight: 700;
    font-size: 52px;
    letter-spacing: 1px;
  }
  /* Front side */
  .card-front {
    left: 760px; top: 164px;
    width: 350px; height: 600px;
    background: var(--paper);
  }
  .brand {
    position: absolute;
    right: 34px; top: 60px;
    display: flex; align-items: center; gap: 14px;
  }
  .brand .dot {
    width: 46px; height: 46px; border-radius: 50%;
    background: var(--orange);
  }
  .brand .name {
    color: var(--navy);
    font-weight: 700;
    font-size: 34px;
    letter-spacing: 1px;
  }
  .name-band {
    position: absolute;
    left: 0; right: 0; top: 190px; height: 78px;
    background: var(--navy);
    text-align: right;
    padding: 12px 30px 0 0;
  }
  .name-band .person {
    font-family: "Cinzel", Georgia, serif;
    font-weight: 700;
    color: var(--orange);
    font-size: 27px;
    letter-spacing: 1px;
    line-height: 1.1;
  }
  .name-band .role {
    font-family: "Cinzel", Georgia, serif;
    font-weight: 500;
    color: #ffffff;
    font-size: 14px;
    margin-top: 4px;
  }
  .contact {
    position: absolute;
    right: 30px; top: 300px;
    text-align: right;
  }
  .contact .icons { display: flex; justify-content: flex-end; gap: 10px; margin-bottom: 14px; }
  .contact .icons svg { width: 20px; height: 20px; }
  .contact p {
    color: var(--ink);
    font-weight: 400;
    font-size: 18px;
    line-height: 1.5;
  }
  .social {
    position: absolute;
    right: 30px; top: 468px;
    display: flex; gap: 12px;
  }
  .social span { width: 26px; height: 26px; border-radius: 50%; }
  .social .alt { background: var(--orange); }
  .social .main { background: var(--navy); }
  .footer-rule {
    position: absolute;
    left: 24px; right: 24px; top: 530px;
    height: 1px; background: var(--rule);
  }
</style>
</head>
<body>
  <section class="card card-back">
    <div class="emboss"></div>
    <div class="wordmark">PIMORTEX</div>
  </section>

  <section class="card card-front">
    <div class="brand">
      <span class="dot"></span>
      <span class="name">PIMORTEX</span>
    </div>

    <div class="name-band">
      <div class="person">DAREN HOLT</div>
      <div class="role">Founder/CEO</div>
    </div>

    <div class="contact">
      <div class="icons">
        <svg viewBox="0 0 20 20" aria-label="phone">
          <path d="M5 3 L8 3 L9 7 L7 8.5 C8 11 9.5 12.5 11.5 13 L13 11 L17 12 L17 15 C17 16 16 17 15 17 C8.5 16.5 3.5 11.5 3 5 C3 4 4 3 5 3 Z" fill="var(--navy)"/>
        </svg>
        <svg viewBox="0 0 20 20" aria-label="email">
          <circle cx="10" cy="10" r="9" fill="var(--orange)"/>
          <circle cx="10" cy="10" r="3" fill="none" stroke="#fff" stroke-width="1.6"/>
          <path d="M13 7 L13 11.5 C13 13 15 13 15 11 C15 7 12.5 5 10 5 C7 5 5 7.5 5 10 C5 13 7.5 15 10 15 C11.2 15 12 14.7 12.8 14.2" fill="none" stroke="#fff" stroke-width="1.4"/>
        </svg>
        <svg viewBox="0 0 20 20" aria-label="website">
          <circle cx="10" cy="10" r="9" fill="var(--navy)"/>
          <circle cx="10" cy="10" r="5.5" fill="none" stroke="#fff" stroke-width="1.2"/>
          <path d="M4.5 10 H15.5 M10 4.5 C7.5 7 7.5 13 10 15.5 M10 4.5 C12.5 7 12.5 13 10 15.5" fill="none" stroke="#fff" stroke-width="1"/>
        </svg>
      </div>
      <p>000 481 7730</p>
      <p>info@pimortex.com</p>
      <p>www.pimortex.com</p>
    </div>

    <div class="social">
      <span class="alt"></span>
      <span class="main"></span>
      <span class="alt"></span>
    </div>

    <div class="footer-rule"></div>
  </section>
</body>
</html>
```